New Business Card Design for Manufacturing

We are an engineering/manufacturing company that offers Advanced machining/assembly/engineering services, as well as innovative products for the heavy duty engine cooling markets.

We are looking to get a new business card designed that is clean and modern looking, but still fits the wide range of technical/skilled work we do.

- We hope to use this design as the base for other design work in new Presentations, web, and print work.

Industry/Entity Type

Engineering

Contact Information for Business Card

Our preferred color of blue is (RGB) 22/71/159 but can vary slightly from that color. Our content will be our Logo and full company name (Fabricated Tooling Works, Inc.), company address, name, job title, phone number with extension, cell number, fax number, website, and email address on the cards.
We'd like the full company name next to the logo, but we are open to other interpretations of that layout.
Preferably, we would like the back side to be clean with just our logo, and the front to contain all of the contact information.

Colors
2f74b4
0355a3
85abd2

Requirements
Must have
• - Logo, company name, needed content - We are open to interpretation beyond that.
• - Standard size business card.
• - Horizontal orientation.
• - Enough space for lengthy names / job titles (for example, a job title could read "Directory of Human Resources" or "V.P. of Governmental Affairs"). We need this to look clean, whether the title be short (CEO) or long (as described above).

```html
<!DOCTYPE html>
<html lang="en">
<head>
<meta charset="utf-8">
<title>Fabricated Tooling Works – Business Card</title>
<link rel="stylesheet" href="https://fonts.googleapis.com/css2?family=Open+Sans:wght@400;600;700;800&display=swap">
<style>
  :root {
    --stage: #2b2c2f;
    --blue: #16479f;
    --blue-deep: #0355a3;
    --blue-mid: #2f74b4;
    --blue-light: #85abd2;
    --blue-bright: #1b8ad4;
    --paper: #ffffff;
    --paper-shade: #eef2f7;
  }
  * { box-sizing: border-box; margin: 0; padding: 0; }
  html, body { width: 1200px; height: 1200px; overflow: hidden; }
  body {
    background: var(--stage);
    font-family: "Open Sans", Arial, sans-serif;
    display: flex;
    flex-direction: column;
    align-items: center;
    justify-content: center;
    gap: 56px;
  }
  .card {
    position: relative;
    width: 900px;
    height: 514px;
    overflow: hidden;
    box-shadow: 0 12px 30px rgba(0,0,0,.45);
  }

  /* ---------- Front ---------- */
  .card--front { background: var(--blue); }
  .front__top {
    position: absolute; left: 0; top: 0; width: 100%; height: 150px;
    background: linear-gradient(90deg, var(--blue) 0%, var(--blue-deep) 100%);
  }
  .front__white {
    position: absolute; left: 0; top: 150px; width: 100%; height: 236px;
    background: linear-gradient(90deg, var(--paper) 0%, var(--paper-shade) 100%);
  }
  .front__bottom {
    position: absolute; left: 0; top: 386px; width: 100%; height: 128px;
    background: linear-gradient(90deg, var(--blue-mid) 0%, var(--blue) 100%);
  }
  .brand-mark {
    position: absolute; left: 44px; top: 22px;
    color: var(--paper);
    font-weight: 800;
    font-size: 96px;
    line-height: 1;
    letter-spacing: 2px;
  }
  .company-name {
    position: absolute; right: 40px; top: 18px;
    color: var(--paper);
    font-weight: 800;
    font-size: 31px;
    line-height: 1.12;
    letter-spacing: 1px;
    text-transform: uppercase;
  }
  .company-name .suffix { font-size: 15px; font-weight: 700; margin-left: 4px; }
  .person {
    position: absolute; left: 44px; top: 182px;
    color: var(--blue);
  }
  .person__name { font-size: 34px; font-weight: 700; line-height: 1.1; }
  .person__title { font-size: 16px; font-weight: 600; margin-top: 4px; }
  .contacts {
    position: absolute; left: 500px; top: 178px;
    color: var(--blue);
    font-size: 16px;
    line-height: 1.4;
    list-style: none;
  }
  .contacts li { display: flex; align-items: flex-start; gap: 10px; }
  .contacts .icon { width: 16px; height: 16px; margin-top: 3px; flex: none; fill: var(--blue); }
  .contacts .no-icon { padding-left: 26px; }
  .website {
    position: absolute; left: 44px; top: 418px;
    color: var(--paper);
    font-size: 44px; font-weight: 700;
  }

  /* ---------- Back ---------- */
  .card--back {
    background: radial-gradient(ellipse at 55% 45%, var(--blue-bright) 0%, var(--blue-deep) 55%, var(--blue) 100%);
  }
  .back__rule {
    position: absolute; left: 0; width: 100%; height: 6px;
    background: var(--paper);
  }
  .back__rule--top { top: 92px; }
  .back__rule--bottom { top: 416px; }
  .back__mark {
    position: absolute; left: 0; top: 0; width: 100%; height: 100%;
    display: flex; align-items: center; justify-content: center;
    color: var(--paper);
    font-weight: 800; font-size: 150px; letter-spacing: 4px;
  }
</style>
</head>
<body>

  <section class="card card--front" aria-label="Business card front">
    <div class="front__top"></div>
    <div class="front__white"></div>
    <div class="front__bottom"></div>

    <div class="brand-mark">FTW</div>
    <div class="company-name">
      Fabricated<br>Tooling<br>Works<span class="suffix">INC</span>
    </div>

    <div class="person">
      <div class="person__name">Full Name</div>
      <div class="person__title">Office</div>
    </div>

    <ul class="contacts">
      <li>
        <svg class="icon" viewBox="0 0 16 16" aria-hidden="true"><path d="M3.6 1.2l2.3 2.6-1.3 1.9c.9 2 2.4 3.6 4.5 4.6l1.9-1.3 2.6 2.3-1.2 2.4C7.2 13.5 2.5 8.8 1.2 3.6z"/></svg>
        <span>Tel. +123 4567 8910</span>
      </li>
      <li class="no-icon">Fax. +123 4567 8910</li>
      <li class="no-icon">Fax. +123 4567 8910</li>
      <li>
        <svg class="icon" viewBox="0 0 16 16" aria-hidden="true"><path d="M1 3h14v10H1z M2.5 4.5v.4L8 8.6l5.5-3.7v-.4z M2.5 6.7v4.8h11V6.7L8 10.4z" fill-rule="evenodd"/></svg>
        <span>youremail@ftworks.com</span>
      </li>
      <li>
        <svg class="icon" viewBox="0 0 16 16" aria-hidden="true"><path d="M8 1a5 5 0 0 0-5 5c0 3.6 5 9 5 9s5-5.4 5-9a5 5 0 0 0-5-5zm0 7a2 2 0 1 1 0-4 2 2 0 0 1 0 4z"/></svg>
        <span>FABRICATED TOOLING WORKS<br>Your Street - N - Your Neighborhood<br>City - EUA</span>
      </li>
    </ul>

    <div class="website">www.yoursite.com</div>
  </section>

  <section class="card card--back" aria-label="Business card back">
    <div class="back__rule back__rule--top"></div>
    <div class="back__rule back__rule--bottom"></div>
    <div class="back__mark">FTW</div>
  </section>

</body>
</html>
```